Pediatric Dental Practice needs a postcard for direct mail advertising

We are looking for a creative and professional double-sided postcard design for a direct mail marketing campaign. Our goal is to attract new families to our pediatric dental practice by conveying a sense of warmth, modern care, and clinical excellence. The design should feel "boutique" and high-end yet remain fun and approachable for parents and children.

```html
<!DOCTYPE html>
<html lang="en">
<head>
<meta charset="utf-8">
<title>Maple Grove Pediatric Dentistry – Postcard</title>
<link href="https://fonts.googleapis.com/css2?family=Poppins:ital,wght@0,400;0,500;0,600;0,700;1,400&display=swap" rel="stylesheet">
<style>
:root{
  --page:#d2ead1;
  --mint-pale:#e6f4e4;
  --mint:#b7dfb8;
  --green:#5bbd75;
  --green-btn:#3f9f5f;
  --green-dark:#17502c;
  --green-text:#1f6a3b;
  --ink:#333a36;
  --white:#ffffff;
}
*{margin:0;padding:0;box-sizing:border-box}
html,body{width:1200px;height:1200px;overflow:hidden}
body{background:var(--page);font-family:"Poppins",sans-serif;position:relative;color:var(--ink)}
.card{position:absolute;left:240px;width:720px;height:480px;overflow:hidden;box-shadow:0 8px 18px rgba(30,70,40,.18)}
.card-front{top:104px;background:linear-gradient(90deg,var(--mint-pale) 0%,#edf6ea 40%,#f3efe4 60%,#e9e2d2 100%)}
.card-back{top:619px;background:var(--white)}
.abs{position:absolute}

/* brand */
.brand{display:flex;align-items:center;gap:14px}
.brand-dot{width:46px;height:46px;border-radius:50%;background:var(--green);flex:none}
.brand-name{font-weight:600;font-size:22px;line-height:1.15;color:var(--ink);letter-spacing:.2px}

/* front */
.front-photo{left:330px;top:0;width:390px;height:440px;background:linear-gradient(160deg,#f6f1e6 0%,#e8e4d4 35%,#b9cfae 60%,#eadfc6 100%)}
.front-fade{left:260px;top:0;width:160px;height:480px;background:linear-gradient(90deg,#edf6ea,rgba(237,246,234,0))}
.front-brand{left:37px;top:36px}
.welcome{left:31px;top:118px;font-size:41px;line-height:49px;color:var(--ink);font-weight:500}
.welcome strong{display:block;font-weight:700;color:var(--green-dark);font-size:44px}
.tagline{left:31px;top:326px;font-style:italic;font-size:24px;line-height:27px;color:var(--green-text)}
.cta{left:31px;top:398px;width:274px;height:42px;border-radius:21px;background:var(--green-btn);color:var(--white);font-weight:700;font-size:15px;display:flex;align-items:center;justify-content:center;box-shadow:0 3px 6px rgba(0,0,0,.15)}
.front-wave{left:0;top:0}
.circle-photo{left:300px;top:195px;width:264px;height:264px;border-radius:50%;border:6px solid var(--mint);background:radial-gradient(circle at 50% 40%,#5fa6a0 0%,#7fbf8c 35%,#d9c7a8 70%,#efe6d6 100%)}
.front-url{right:30px;top:437px;color:var(--white);font-size:14px}

/* back */
.back-wave{left:0;top:0}
.back-brand-box{left:30px;top:0;width:322px;height:115px;background:var(--white);border-radius:0 0 14px 14px;box-shadow:0 3px 8px rgba(0,0,0,.08);display:flex;align-items:center;padding-left:16px}
.back-title{left:30px;top:122px;font-weight:700;font-size:32px;line-height:44px;color:var(--green-dark);white-space:nowrap}
.back-copy{left:30px;top:167px;width:400px;font-size:12.6px;line-height:18.6px;color:var(--ink)}
.benefits{left:30px;top:230px;list-style:none}
.benefits li{display:flex;align-items:center;gap:8px;height:29px;font-size:16.8px;color:var(--green-text);white-space:nowrap}
.tick{width:19px;height:19px;flex:none}
.contact{left:30px;top:382px;width:300px;height:80px;background:var(--white);border-radius:6px;box-shadow:0 2px 8px rgba(0,0,0,.12);border-left:10px solid var(--green);padding:6px 0 0 8px}
.contact p{display:flex;align-items:center;gap:8px;font-size:10.6px;line-height:16.8px;height:16.8px;color:#1c1c1c;white-space:nowrap}
.contact svg{width:11px;height:11px;flex:none}
.divider{left:433px;top:78px;width:4px;height:325px;background:var(--mint)}
.stamp{left:579px;top:30px;width:110px;height:128px;border:1.5px solid #333}
.address-line{left:475px;width:214px;height:1.5px;background:#333}
</style>
</head>
<body>

<section class="card card-front">
  <div class="abs front-photo" role="img" aria-label="Bright pediatric dental operatory with a window, dental light and a wall-mounted screen"></div>
  <div class="abs front-fade"></div>
  <svg class="abs front-wave" width="720" height="480" viewBox="0 0 720 480">
    <path d="M0 440 C120 470 260 470 380 448 C500 425 600 405 720 415 L720 480 L0 480 Z" fill="#d7efd6"/>
    <path d="M0 438 C120 462 250 470 380 455 C500 440 610 418 720 428 L720 480 L0 480 Z" fill="var(--green)"/>
  </svg>
  <div class="abs circle-photo" role="img" aria-label="Smiling dentist showing young children how to brush a plush toy's teeth"></div>

  <div class="abs brand front-brand">
    <span class="brand-dot"></span>
    <span class="brand-name">Maple Grove<br>Pediatric Dentistry</span>
  </div>
  <h1 class="abs welcome">Welcome to<strong>Maple Grove</strong>Pediatric<br>Dentistry</h1>
  <p class="abs tagline">Where Smiles<br>Grow with Care!</p>
  <div class="abs cta">Schedule Your First Visit Today!</div>
  <span class="abs front-url">maplegrovekids.com</span>
</section>

<section class="card card-back">
  <svg class="abs back-wave" width="720" height="480" viewBox="0 0 720 480">
    <rect width="720" height="480" fill="#cfe9d2"/>
    <path d="M0 0 L720 0 L720 30 C640 40 560 10 470 40 C400 60 340 50 300 45 L0 60 Z" fill="#bfe1c3"/>
    <path d="M0 110 C40 80 120 60 260 55 C380 50 470 10 560 22 C640 32 700 60 720 80 L720 400 C640 430 560 450 470 445 C360 440 250 445 150 455 C80 460 30 450 0 440 Z" fill="var(--white)"/>
    <path d="M560 480 C600 440 660 420 720 420 L720 480 Z" fill="#bfe1c3"/>
  </svg>

  <div class="abs back-brand-box">
    <div class="brand">
      <span class="brand-dot"></span>
      <span class="brand-name">Maple Grove<br>Pediatric Dentistry</span>
    </div>
  </div>

  <h2 class="abs back-title">Caring for Little Smiles</h2>
  <p class="abs back-copy">Maple Grove, we create a fun, safe space where children feel comfortable. Our experienced pediatric team is dedicated to building healthy habits that last a lifetime.</p>

  <ul class="abs benefits">
    <li><svg class="tick" viewBox="0 0 20 20"><circle cx="10" cy="10" r="10" fill="var(--green)"/><path d="M5.5 10.3l3 3 6-6.3" stroke="#fff" stroke-width="2.4" fill="none" stroke-linecap="round" stroke-linejoin="round"/></svg>Child-friendly, calming environment</li>
    <li><svg class="tick" viewBox="0 0 20 20"><circle cx="10" cy="10" r="10" fill="var(--green)"/><path d="M5.5 10.3l3 3 6-6.3" stroke="#fff" stroke-width="2.4" fill="none" stroke-linecap="round" stroke-linejoin="round"/></svg>Preventative care &amp; oral health education</li>
    <li><svg class="tick" viewBox="0 0 20 20"><circle cx="10" cy="10" r="10" fill="var(--green)"/><path d="M5.5 10.3l3 3 6-6.3" stroke="#fff" stroke-width="2.4" fill="none" stroke-linecap="round" stroke-linejoin="round"/></svg>Experienced staff in pediatric dentistry</li>
    <li><svg class="tick" viewBox="0 0 20 20"><circle cx="10" cy="10" r="10" fill="var(--green)"/><path d="M5.5 10.3l3 3 6-6.3" stroke="#fff" stroke-width="2.4" fill="none" stroke-linecap="round" stroke-linejoin="round"/></svg>Gentle approach for anxious little patients</li>
    <li><svg class="tick" viewBox="0 0 20 20"><circle cx="10" cy="10" r="10" fill="var(--green)"/><path d="M5.5 10.3l3 3 6-6.3" stroke="#fff" stroke-width="2.4" fill="none" stroke-linecap="round" stroke-linejoin="round"/></svg>Same-day appointments available</li>
  </ul>

  <div class="abs contact">
    <p><svg viewBox="0 0 12 12"><circle cx="6" cy="6" r="6" fill="var(--green)"/><path d="M4 3.2l1 1.3-.6.8c.4.8 1 1.4 1.8 1.8l.8-.6 1.3 1-.6 1c-2.4-.4-4-2-4.4-4.4z" fill="#fff"/></svg>(555) 014-2290</p>
    <p><svg viewBox="0 0 12 12"><circle cx="6" cy="6" r="6" fill="var(--green)"/><rect x="3" y="4" width="6" height="4.2" fill="none" stroke="#fff" stroke-width=".9"/><path d="M3 4l3 2.3L9 4" fill="none" stroke="#fff" stroke-width=".9"/></svg>hello@maplegrovekids.com</p>
    <p><svg viewBox="0 0 12 12"><circle cx="6" cy="6" r="6" fill="var(--green)"/><circle cx="6" cy="6" r="3.2" fill="none" stroke="#fff" stroke-width=".8"/><path d="M2.8 6h6.4M6 2.8c-1.4 1.8-1.4 4.6 0 6.4M6 2.8c1.4 1.8 1.4 4.6 0 6.4" fill="none" stroke="#fff" stroke-width=".8"/></svg>www.maplegrovekids.com</p>
    <p><svg viewBox="0 0 12 12"><circle cx="6" cy="6" r="6" fill="var(--green)"/><path d="M6 2.5a2.3 2.3 0 0 1 2.3 2.3C8.3 6.6 6 9.3 6 9.3S3.7 6.6 3.7 4.8A2.3 2.3 0 0 1 6 2.5z" fill="#fff"/><circle cx="6" cy="4.8" r=".9" fill="var(--green)"/></svg>48 Orchard Lane, Suite 210 Fairhaven, CT 06500</p>
  </div>

  <div class="abs divider"></div>
  <div class="abs stamp"></div>
  <div class="abs address-line" style="top:258px"></div>
  <div class="abs address-line" style="top:306px"></div>
  <div class="abs address-line" style="top:355px"></div>
</section>

</body>
</html>
```